Dalwin Tasker Construction LLC

I like to have a business card the is unique, very professional and the it will projected the best first impression of me and my company

Target Market(s)

Remodeling, new constitution

Industry/Entity Type

Business

Font styles to use
Script

Requirements
Must have
• My company name email and phone number
Nice to have
• A logo maybe

```html
<!DOCTYPE html>
<html lang="en">
<head>
<meta charset="utf-8">
<title>Dalwin Tasker Construction LLC – Business Card</title>
<link rel="stylesheet" href="https://fonts.googleapis.com/css2?family=PT+Sans:wght@400;700&family=Questrial&display=swap">
<style>
  :root {
    --stage: #2b2b2d;
    --card-dark: #0b0b0d;
    --card-glow: #1d3f9e;
    --card-light: #ececee;
    --card-light-edge: #d4d4d8;
    --brand-blue: #1b3190;
    --brand-orange: #e2621b;
    --ink: #1a1a1a;
    --white: #ffffff;
  }
  * { box-sizing: border-box; margin: 0; padding: 0; }
  html, body { width: 1200px; height: 900px; overflow: hidden; }
  body {
    background: var(--stage);
    font-family: "PT Sans", sans-serif;
    position: relative;
  }
  .presentation-title {
    position: absolute;
    top: 34px; right: 96px;
    font-family: "Questrial", sans-serif;
    font-size: 46px;
    font-weight: 400;
    color: var(--white);
    letter-spacing: -0.5px;
  }
  .card {
    position: absolute;
    border-radius: 22px;
    overflow: hidden;
  }
  .card-front {
    background: radial-gradient(ellipse at 50% 35%, var(--card-glow) 0%, #0f1d4a 35%, var(--card-dark) 75%);
    color: var(--white);
    display: flex; flex-direction: column; align-items: center;
  }
  .card-back {
    background: linear-gradient(135deg, var(--white) 0%, var(--card-light) 55%, var(--card-light-edge) 100%);
    color: var(--ink);
  }
  .front-large { left: 290px; top: 185px; width: 560px; height: 270px; }
  .back-large { left: 62px; top: 470px; width: 560px; height: 330px; }
  .front-small { left: 880px; top: 125px; width: 205px; height: 117px; border-radius: 10px; }
  .back-small { left: 880px; top: 257px; width: 205px; height: 117px; border-radius: 10px; }

  .brand { display: flex; align-items: center; gap: 12px; }
  .brand-mark { background: var(--brand-orange); flex: none; }
  .brand-name { font-weight: 700; line-height: 1.05; }
  .card-front .brand-name { color: var(--white); }
  .card-back .brand-name { color: var(--brand-blue); }

  .front-large .brand { margin-top: 96px; }
  .front-large .brand-mark { width: 26px; height: 26px; }
  .front-large .brand-name { font-size: 25px; max-width: 300px; }
  .front-large .web { position: absolute; bottom: 22px; font-size: 14px; }

  .back-large .brand { position: absolute; left: 36px; top: 130px; }
  .back-large .brand-mark { width: 22px; height: 22px; }
  .back-large .brand-name { font-size: 21px; max-width: 190px; }

  .contact { position: absolute; white-space: nowrap; }
  .back-large .contact { left: 296px; top: 92px; font-size: 16px; line-height: 1.35; }
  .contact .person { font-size: 17px; }
  .contact .person strong { font-weight: 700; }
  .contact .role { font-size: 12px; }
  .contact .row { display: flex; align-items: flex-start; gap: 8px; }
  .contact .gap { margin-top: 16px; }
  .contact svg { flex: none; margin-top: 3px; }

  .front-small .brand { margin-top: 30px; gap: 6px; }
  .front-small .brand-mark { width: 10px; height: 10px; }
  .front-small .brand-name { font-size: 9px; max-width: 110px; }
  .front-small .web { position: absolute; bottom: 9px; font-size: 5px; }

  .back-small .brand { position: absolute; left: 14px; top: 42px; gap: 5px; }
  .back-small .brand-mark { width: 9px; height: 9px; }
  .back-small .brand-name { font-size: 7.5px; max-width: 66px; }
  .back-small .contact { left: 100px; top: 36px; font-size: 5.5px; line-height: 1.35; }
  .back-small .contact .person { font-size: 6.5px; }
  .back-small .contact .role { font-size: 5px; }
  .back-small .contact .row { gap: 3px; }
  .back-small .contact .gap { margin-top: 4px; }
  .back-small .contact svg { margin-top: 1px; width: 5px; height: 5px; }
</style>
</head>
<body>
  <h1 class="presentation-title">Dalwin Tasker Construction LLC</h1>

  <section class="card card-front front-large">
    <div class="brand"><span class="brand-mark"></span><span class="brand-name">Dalwin Tasker Construction LLC</span></div>
    <p class="web">www.dalwintasker.com</p>
  </section>

  <section class="card card-back back-large">
    <div class="brand"><span class="brand-mark"></span><span class="brand-name">Dalwin Tasker Construction LLC</span></div>
    <div class="contact">
      <p class="person"><strong>Marcus Hale</strong> | <span class="role">President</span></p>
      <p class="row"><svg width="12" height="12" viewBox="0 0 12 12"><rect x="0" y="2" width="12" height="8" fill="var(--brand-orange)"/><path d="M0 2 L6 7 L12 2" stroke="#fff" fill="none"/></svg>marcushale@dalwintasker.com</p>
      <p class="row gap"><svg width="14" height="14" viewBox="0 0 14 14"><circle cx="7" cy="7" r="7" fill="var(--brand-orange)"/><path d="M4.5 3.5 Q4 8 9.5 10" stroke="#fff" stroke-width="2" fill="none"/></svg>555.014.2368</p>
      <p class="row"><svg width="14" height="14" viewBox="0 0 14 14"><rect x="1" y="2" width="12" height="10" rx="1" fill="var(--brand-orange)"/><rect x="3" y="4" width="8" height="2" fill="#fff"/></svg>555.014.2368</p>
      <p class="row"><svg width="14" height="16" viewBox="0 0 14 16"><path d="M7 16 C2 9 1 7 1 6 A6 6 0 0 1 13 6 C13 7 12 9 7 16Z" fill="var(--brand-orange)"/><circle cx="7" cy="6" r="2.2" fill="#fff"/></svg><span>4120 W. Alder Creek Rd.<br>Suite 210, PMB 38<br>Linford, MI 48290</span></p>
    </div>
  </section>

  <section class="card card-front front-small">
    <div class="brand"><span class="brand-mark"></span><span class="brand-name">Dalwin Tasker Construction LLC</span></div>
    <p class="web">www.dalwintasker.com</p>
  </section>

  <section class="card card-back back-small">
    <div class="brand"><span class="brand-mark"></span><span class="brand-name">Dalwin Tasker Construction LLC</span></div>
    <div class="contact">
      <p class="person"><strong>Marcus Hale</strong> | <span class="role">President</span></p>
      <p class="row"><svg viewBox="0 0 12 12"><rect x="0" y="2" width="12" height="8" fill="var(--brand-orange)"/></svg>marcushale@dalwintasker.com</p>
      <p class="row gap"><svg viewBox="0 0 14 14"><circle cx="7" cy="7" r="7" fill="var(--brand-orange)"/></svg>555.014.2368</p>
      <p class="row"><svg viewBox="0 0 14 14"><rect x="1" y="2" width="12" height="10" fill="var(--brand-orange)"/></svg>555.014.2368</p>
      <p class="row"><svg viewBox="0 0 14 16"><path d="M7 16 C2 9 1 7 1 6 A6 6 0 0 1 13 6 C13 7 12 9 7 16Z" fill="var(--brand-orange)"/></svg><span>4120 W. Alder Creek Rd.<br>Suite 210, PMB 38<br>Linford, MI 48290</span></p>
    </div>
  </section>
</body>
</html>
```